Brightleaf Wellness Website Design

About The Client:
Brightleaf Wellness is a sugar-free foods chain store providing services to Diabetics. They focus on the China domestic market. They describe themselves as being the 3rd space for Diabetics, the space between hospital and the home that help improve the quality of life for people wit Diabetes (see attached infographics).

They regularly hold education and advice events throughout the China. Brightleaf Wellness distribute a wide product range of food that is suitable for diabetic people. Brightleaf Wellness operate as a Franchise, providing business development services and Industry knowledge. They are actively seeking business partnerships at present.

The Brief:
Design a Home page and secondary information page(PSD only no code) that communicates our company services and company philosophy(3rd Space).
The final design should communicate 'Health, Social Responsibility and Professionalism'.
Colour scheme should orientate around Blue and White, see attached logo.

Websites we like:

http://link.venomira.com/home/

https://www.paxtunel.com/

http://dev.zorvik.com/
Updates

Hello all, the client has advised us that he want to display the professional advice service available for diabetic people more so than a food distributor. The client is also hoping to use his website as a marketing platform to attract affiliates and build partnerships as part of Brightleaf Wellness's business expansion strategy.

So can you make the page more corporate, reliable and professional. Use images of experts/doctors interacting with patients and also training/knowledge transfer images.

Thanks

Hello all, could you include stock images of both Chinese and Caucasians

Yeaahhh, Infographics and photos have been uploaded. Feel free to use them in your designs and also as references.

Target Market(s)

The target market is Chinese B2B in the Diabetics industry and Entrepreneurs looking to cooperate with Brightleaf Wellness.

Industry/Entity Type

Education

Requirements
Must have
• menu navigation with 7-8 sections,
a full screen background image,
Social Media icons,
Logo in top left,
Site search.
Nice to have
• The website must be clear and easy to use, less complicated.

See attached files of some Brightleaf Wellness infographics. Feel free to include elements of these into the design.
Should not have
• Should not use stock images of people from any other country, the client wants stock images of Chinese people only. Avoid photos showing obesity.

```html
<!DOCTYPE html>
<html lang="en">
<head>
<meta charset="utf-8">
<title>Brightleaf Wellness – Home</title>
<link href="https://fonts.googleapis.com/css2?family=Roboto+Condensed:wght@400;700&display=swap" rel="stylesheet">
<style>
:root{
  --blue:#1b8fd6;
  --blue-dark:#0a6fae;
  --blue-light:#3fb2ee;
  --heading:#0c6aa6;
  --red:#e2313c;
  --red-dark:#c5202b;
  --text:#3f3f3f;
  --muted:#555;
  --page:#f7f7f7;
  --card:#f1f2f2;
  --line:#c9c9c9;
  --white:#fff;
}
*{box-sizing:border-box;margin:0;padding:0}
html,body{width:1200px;height:1142px;overflow:hidden}
body{position:relative;background:var(--page);font-family:"Roboto Condensed",Arial,sans-serif;color:var(--text)}
.site-header{position:absolute;left:0;top:0;width:1200px;height:105px;background:var(--white);border-bottom:1px solid #ddd}
.brand{position:absolute;left:181px;top:34px;display:flex;align-items:center;gap:9px;font-size:24px;font-weight:700;color:var(--blue)}
.brand-mark{width:22px;height:22px;background:var(--blue)}
.social{position:absolute;right:350px;top:27px;display:flex;gap:8px;font-size:12px;line-height:16px;color:var(--blue);white-space:nowrap}
.search{position:absolute;left:864px;top:19px;width:181px;height:32px;border:1px solid #cfcfcf;background:var(--white);box-shadow:inset 0 0 0 2px #f2f2f2}
.search span{position:absolute;left:10px;top:7px;font-size:14px;color:#777}
.search svg{position:absolute;right:9px;top:7px}
.main-nav{position:absolute;left:445px;top:69px;display:flex}
.main-nav a{display:block;padding:0 15px;height:36px;font-size:16px;color:#555;text-decoration:none;line-height:22px}
.main-nav a.active{color:var(--blue);border-bottom:4px solid var(--blue)}
.hero{position:absolute;left:0;top:105px;width:1200px;height:381px;background:linear-gradient(90deg,#2e6f6c 0%,#b0662a 25%,#e08a2c 45%,#b8682a 60%,#3c7f80 85%,#2c8a8d 100%)}
.hero-photo{position:absolute;inset:0}
.hero-band{position:absolute;left:0;top:244px;width:1200px;height:96px;background:rgba(40,50,55,.72)}
.hero-caption{position:absolute;left:182px;top:265px;font-size:23px;line-height:28px;color:var(--white)}
.hero-caption strong{color:var(--blue-light);font-weight:700}
.hero-dots{position:absolute;left:566px;top:352px;display:flex;gap:3px}
.hero-dots i{width:18px;height:18px;border-radius:50%;background:#666;border:1px solid #555}
.hero-dots i.on{background:var(--blue)}
.feature{position:absolute;top:509px;width:290px;height:247px;background:var(--card);border:1px solid var(--line);text-align:center}
.feature h2{margin-top:14px;font-size:16px;color:var(--heading)}
.feature .thumb{margin:10px auto 0;width:255px;height:102px;border:1px solid #bbb;background:var(--white);padding:5px}
.feature .thumb div{width:100%;height:100%}
.feature p{margin:7px 14px 0;font-size:12.5px;line-height:14.5px;color:var(--muted)}
.btn{display:inline-block;color:var(--white);font-weight:700;text-align:center;border-radius:2px;background:linear-gradient(#4fc0f2,var(--blue) 50%,var(--blue-dark));box-shadow:0 1px 2px rgba(0,0,0,.3)}
.feature .btn{margin-top:10px;width:115px;height:29px;line-height:29px;font-size:12px}
.section-title{position:absolute;font-size:16px;font-weight:400;color:#555;padding-bottom:9px;border-bottom:1px dashed #bbb}
.section-title b{color:var(--heading);font-weight:700}
.welcome-text{position:absolute;left:148px;top:826px;width:575px;font-size:12.5px;line-height:14.8px;color:var(--muted)}
.cta{position:absolute;top:912px;width:192px;height:45px;line-height:45px;font-size:15px;border-radius:4px}
.cta.red{background:linear-gradient(#f0707a,var(--red) 50%,var(--red-dark))}
.field{position:absolute;left:754px;width:294px;border:1px solid #ccc;background:var(--white);font-size:13px;color:#555;padding:7px 5px}
.submit{position:absolute;left:932px;top:965px;width:115px;height:29px;line-height:29px;font-size:12px}
.site-footer{position:absolute;left:0;top:1042px;width:1200px;height:100px;background:var(--white);border-top:1px solid #ddd;text-align:center;font-size:11.5px;line-height:16px;color:#555;padding-top:34px}
</style>
</head>
<body>
<header class="site-header">
  <div class="brand"><span class="brand-mark"></span>Brightleaf Wellness</div>
  <div class="social"><span>Chirpline</span><span>Friendbook</span></div>
  <div class="search"><span>Search</span>
    <svg width="18" height="18" viewBox="0 0 18 18"><circle cx="7" cy="7" r="5.5" fill="none" stroke="#6a7f8a" stroke-width="1.8"/><line x1="11" y1="11" x2="16.5" y2="16.5" stroke="#6a7f8a" stroke-width="2.4"/></svg>
  </div>
  <nav class="main-nav">
    <a class="active">Home</a><a>About Us</a><a>Services</a><a>Food Store</a><a>Our Philosophy</a><a>Events</a><a>Contact Us</a>
  </nav>
</header>

<section class="hero">
  <div class="hero-photo" role="img" aria-label="Supermarket produce aisles with a smiling staff member holding a blue heart"></div>
  <div class="hero-band"></div>
  <p class="hero-caption">We just not only sale food but<br>also made our <strong>Social Responsibilities</strong>.</p>
  <div class="hero-dots"><i class="on"></i><i></i><i></i></div>
</section>

<article class="feature" style="left:147px">
  <h2>Our Philosophy</h2>
  <div class="thumb"><div role="img" aria-label="Advisors consulting with patients at a table" style="background:linear-gradient(90deg,#8a6a58,#d8d0c8,#a9a49c)"></div></div>
  <p>Lorem ipsum dolor sit amet, consectetur adipisicing elit, sed do eiusmod tempor incididunt ut labore et dolore magna aliqua.</p>
  <a class="btn">Know More</a>
</article>
<article class="feature" style="left:452px">
  <h2>Our Services</h2>
  <div class="thumb"><div role="img" aria-label="Staff member working in a bright store kitchen" style="background:linear-gradient(90deg,#c9d3da,#e6e3de,#b9c6cf)"></div></div>
  <p>Lorem ipsum dolor sit amet, consectetur adipisicing elit, sed do eiusmod tempor incididunt ut labore et dolore magna aliqua.</p>
  <a class="btn">Know More</a>
</article>
<article class="feature" style="left:756px">
  <h2>Our Events</h2>
  <div class="thumb"><div role="img" aria-label="Customers at an in-store event among product shelves" style="background:linear-gradient(90deg,#c44b3a,#8fb7d8,#d2a24a)"></div></div>
  <p>Lorem ipsum dolor sit amet, consectetur adipisicing elit, sed do eiusmod tempor incididunt ut labore et dolore magna aliqua.</p>
  <a class="btn">Know More</a>
</article>

<h3 class="section-title" style="left:148px;top:786px;width:594px"><b>Welcome</b> to our site</h3>
<p class="welcome-text">Lorem ipsum dolor sit amet, consectetur adipisicing elit, sed do eiusmod tempor incididunt ut labore et dolore magna aliqua. Lorem ipsum dolor sit amet, consectetur adipisicing elit, sed do eiusmod tempor incididunt ut labore et dolore magna aliqua. Lorem ipsum dolor sit amet, consectetur adipisicing elit, sed do eiusmod tempor incididunt ut labore et dolore magna aliqua.</p>
<a class="btn cta" style="left:148px">OUR TRAINING</a>
<a class="btn cta red" style="left:349px">PERTNERSHIP</a>
<a class="btn cta" style="left:550px">FOR DIABETICS</a>

<h3 class="section-title" style="left:755px;top:786px;width:293px"><b>Query Us</b> to help you</h3>
<div class="field" style="top:828px;height:30px">Email</div>
<div class="field" style="top:866px;height:91px">Query</div>
<a class="btn submit">Submit</a>

<footer class="site-footer">
  <p>Copyright@2013. All rights are reserved.</p>
  <p>Terms &amp; Privacy Policy</p>
</footer>
</body>
</html>
```